My dad's 70th birthday party invite - Greek theme!

My dad isn't actually Greek, but his party will be at a Greek restaurant, so we thought it'd be a fun to have a Greek theme for the invitation to his 70th birthday party.

The invite will be sent out by email, so it needs to look good on screen, AND when it's printed out by the recipients, likely onto A4 paper and put up on a noticeboard/stuck to the fridge as a reminder etc.
Updates

Reason: A designer has asked us to extend the deadline and as we're not in a rush to complete this particular project, we've done so. Thanks everyone for their designs to date.

Target Market(s)

my dad's friends and family - average 50-70years old

Industry/Entity Type

Restaurant

Requirements
Must have
• For: Brannick's 70th birthday
Date: 30 Nov 2013
Time: 7.30pm
Place: Lymora Taverna, 47 Tressendale Road, Mulvaney Park

RSVP by: Friday 1 November
to: kat@pqx-example.com.au
(Please also let us know of any specific dietary requirements eg vegetarian, seafood allergy etc. Thanks. And please, no presents - just really hoping you can join us on the night!)
Nice to have
• Some ideas for you:
- he loves the blue & white of Greece eg white buildings against blue ocean, Greek flag etc
- and red geraniums/pink bouganvillea - quintessential (yet stylish!) Greece
- also, maybe you could use the names of the dishes we'll be having for dinner somehow? ie:
MEZES
Taramosalata
Tzatziki
Skordalia
Hommus
Haloumi
Psití Melitzána
Pita
Eliés
Dolmathes
THALASINA
Chtapódi Psitó
KalamáriaTiganitá
KREATA
Souvlaki
Arní
Lachaniká se Sáltsa - Verrosti
SALATA
Baklava
Paximádi Rolá
Kataifi
Kourabiethes
Greek Coffee

Hope that helps!
Should not have
• We'd prefer a simple colour scheme, ie not too many different colours.

```html
<!DOCTYPE html>
<html lang="en">
<head>
<meta charset="utf-8">
<title>Brannick's 70th Birthday Invitation</title>
<link rel="stylesheet" href="https://fonts.googleapis.com/css2?family=Della+Respira&family=Cormorant+Garamond:ital,wght@1,600;1,700&family=Arimo&display=swap">
<style>
  :root {
    --sea-deep: #123f86;
    --sea-mid: #2b63a8;
    --sky: #6f9fd6;
    --cliff: #a58a72;
    --whitewash: #eef0f2;
    --bloom: #c2337f;
    --bloom-dark: #6c2a3a;
    --invite-pink: #ee6cd6;
    --halo: #ffffff;
    --name-blue: #1d8ee8;
    --menu-red: #ea1512;
    --menu-blue: #1a63d8;
    --menu-panel: rgba(255,255,255,0.72);
    --flag-blue: #1550d6;
  }
  * { margin: 0; padding: 0; box-sizing: border-box; }
  html, body { width: 1200px; height: 849px; overflow: hidden; background: #fff; }
  .invite { position: relative; width: 1200px; height: 849px; overflow: hidden; }

  .scene {
    position: absolute; inset: 0;
    background:
      radial-gradient(ellipse 330px 420px at 860px 560px, var(--bloom) 0%, rgba(194,51,127,0.6) 50%, transparent 100%),
      radial-gradient(ellipse 260px 300px at 700px 800px, var(--bloom) 0%, transparent 100%),
      radial-gradient(ellipse 420px 260px at 420px 560px, var(--whitewash) 0%, rgba(238,240,242,0.7) 45%, transparent 100%),
      radial-gradient(ellipse 260px 140px at 620px 380px, var(--cliff) 0%, transparent 100%),
      radial-gradient(ellipse 200px 360px at 960px 250px, var(--bloom-dark) 0%, transparent 100%),
      linear-gradient(180deg, var(--sky) 0%, var(--sea-mid) 8%, var(--sea-deep) 45%, var(--sea-mid) 100%);
  }

  .flag { position: absolute; left: 0; top: 22px; width: 298px; height: 186px; }

  .headline {
    position: absolute; left: 330px; width: 660px; text-align: center;
    font-family: "Della Respira", serif; color: var(--invite-pink);
    text-shadow: 0 0 2px var(--halo), 0 0 2px var(--halo), 0 0 4px var(--halo);
    white-space: nowrap;
  }
  .headline--greeting { top: 34px; font-size: 37px; }
  .headline--join { top: 92px; font-size: 37px; }
  .headline--honour { top: 138px; font-size: 33px; }
  .honoree {
    position: absolute; left: 330px; width: 660px; top: 188px; text-align: center;
    font-family: "Cormorant Garamond", serif; font-style: italic; font-weight: 700;
    font-size: 92px; line-height: 1; color: var(--name-blue);
    text-shadow: 0 0 2px var(--halo), 0 0 3px var(--halo), 2px 2px 3px rgba(0,0,0,0.35);
  }
  .headline--age { top: 282px; font-size: 34px; }
  .age-number {
    font-family: "Cormorant Garamond", serif; font-style: italic; font-weight: 600;
    font-size: 48px; color: var(--name-blue);
  }

  .details {
    position: absolute; left: 25px; width: 990px;
    font-family: "Della Respira", serif; color: var(--invite-pink);
    text-shadow: 0 0 2px var(--halo), 0 0 2px var(--halo), 0 0 4px var(--halo);
    white-space: nowrap;
  }
  .details--when { top: 385px; font-size: 32px; }
  .details--where { top: 432px; font-size: 31px; }
  .details--rsvp { top: 545px; font-size: 30px; }
  .details--note { top: 598px; font-size: 29px; line-height: 52px; white-space: normal; }

  .menu {
    position: absolute; left: 1030px; top: 0; width: 170px; height: 849px;
    background: var(--menu-panel); border-left: 2px solid var(--halo);
  }
  .menu-heading {
    position: absolute; left: 1010px; width: 190px; height: 50px;
    background: var(--menu-red); color: #fff; text-align: center;
    font-family: "Della Respira", serif; font-size: 30px; line-height: 52px;
  }
  .menu-list {
    position: absolute; left: 1043px; list-style: none;
    font-family: "Arimo", Arial, sans-serif; font-size: 16.5px; line-height: 24.5px;
    color: var(--menu-blue); white-space: nowrap;
  }
  .menu-list--wrap { white-space: normal; width: 150px; }
</style>
</head>
<body>
<main class="invite">
  <div class="scene" role="img" aria-label="Photograph of a Greek island: whitewashed buildings on a cliff above deep blue sea, with pink bougainvillea in the foreground"></div>

  <svg class="flag" viewBox="0 0 298 186" role="img" aria-label="Greek flag">
    <rect width="298" height="186" fill="#fff"/>
    <g fill="var(--flag-blue)">
      <rect y="0" width="298" height="20.7"/>
      <rect y="41.3" width="298" height="20.7"/>
      <rect y="82.7" width="298" height="20.7"/>
      <rect y="124" width="298" height="20.7"/>
      <rect y="165.3" width="298" height="20.7"/>
      <rect width="103" height="103.4"/>
    </g>
    <rect x="41.3" width="20.7" height="103.4" fill="#fff"/>
    <rect y="41.3" width="103" height="20.7" fill="#fff"/>
  </svg>

  <p class="headline headline--greeting">Its a great Celebration !!</p>
  <p class="headline headline--join">Please join us for food and fun</p>
  <p class="headline headline--honour">in honour of</p>
  <h1 class="honoree">Brannick</h1>
  <p class="headline headline--age">who is turning <span class="age-number">70</span> !!</p>

  <p class="details details--when">On 30 November, 2013 at 7.30pm</p>
  <p class="details details--where">Lymora Taverna, 47 Tressendale Road, Mulvaney Park</p>
  <p class="details details--rsvp">RSVP by Friday 1 November, 2013 / kat@pqx-example.com.au</p>
  <p class="details details--note">(Please also let us know of any specific dietary<br>requirements eg vegetarian, seafood allergy etc. Thanks.<br>And please, no presents - just really hoping you can join us<br>on the night!)</p>

  <aside class="menu" aria-label="Dinner menu"></aside>

  <h2 class="menu-heading" style="top:18px">MEZES</h2>
  <ul class="menu-list" style="top:80px">
    <li>Taramosalata</li><li>Tzatziki</li><li>Skordalia</li><li>Hommus</li><li>Haloumi</li>
    <li>Psití Melitzána</li><li>Pita</li><li>Eliés</li><li>Dolmathes</li>
  </ul>

  <h2 class="menu-heading" style="top:322px">THALASINA</h2>
  <ul class="menu-list" style="top:382px; left:1040px; line-height:28px">
    <li>Chtapódi Psitó</li><li>KalamáriaTiganitá</li>
  </ul>

  <h2 class="menu-heading" style="top:457px">KREATA</h2>
  <ul class="menu-list menu-list--wrap" style="top:513px; left:1046px; line-height:23.5px">
    <li>Souvlaki</li><li>Arní</li><li>Lachaniká se Sáltsa- Verrosti</li>
  </ul>

  <h2 class="menu-heading" style="top:628px">SALATA</h2>
  <ul class="menu-list" style="top:690px; left:1046px; line-height:25.5px">
    <li>Baklava</li><li>Paximádi Rolá</li><li>Kataifi</li><li>Kourabiethes</li><li>Greek Coffee</li>
  </ul>
</main>
</body>
</html>
```